New Design for our Credit Cards tank.

Our company has petrol stations in Spain and the rest of Europe. We are specialized on the international transport companies. For This We Have our own "credit cards tank" With These cards you can refill in different countries (all over Europe) fast, save and cheap. We would like to redesign our credit cards tank. We are looking for something more modern, elegant and clean. We have three card types: - Spanish Card (Spain Card): This card is for customers who make refills at our service stations in Spain. This card is for Diesel product and used by transport companies. The printer prints the data That on This card can print in white. The fields we are print on the card, card number, holder, registration number and expiration date. - Europe Card (Europe Card): This card is for customers who refills at our service stations in Europe. The printer prints the data That on This card can not print in white. The fields we are print on the card, card number, holder, registration number and expiration date. - Red Card (Gasoleo Bonificado): This card is for a Customer WHO refills Red Diesel for a refrigerator units in our service stations in Spain. The printer prints the data That on This card can print in white. The fields we are print on the card, card number, holder, registration number and expiration date. Very important for us is That on the back side, you respect the text shown on the cards and the magnetic stripe zone. Of course Also the name of the company VERDAPUMP must be seen there. Also would be great if our colors (its blue colors) will be respected. If You have any questions or Suggest we are pleased to get your comments or contacts. Thanks in advance Verdapump

Target Market(s)

Our customers

Industry/Entity Type

Credit Card

Font styles to use
Sans Serif

Colors
3176b5
0255a3
85acd3
cedeed
85cae6
33a6d7
0692cd
f59195
f04a50

Requirements
Must have
• The only thing we Have to keep the fields on front and back text. The credit card 85mm x 54mm are meassures.

```html
<!DOCTYPE html>
<html lang="es">
<head>
<meta charset="utf-8">
<title>Verdapump — Europe Card</title>
<link rel="stylesheet" href="https://fonts.googleapis.com/css2?family=Open+Sans:wght@400;600;700&family=Share+Tech+Mono&display=swap">
<style>
  :root {
    --page: #46474a;
    --card-dark: #1f2022;
    --card-dark-2: #2a2b2e;
    --map-grey: #4b4c50;
    --brand-blue: #0255a3;
    --brand-blue-mid: #3176b5;
    --navy: #123a63;
    --accent-orange: #e0711c;
    --back-orange-1: #b9862a;
    --back-orange-2: #c9701a;
    --stripe: #111112;
    --text-light: #f2f2f2;
    --text-muted: #9a9b9e;
    --emboss: #d9dadc;
    --back-text: #2a1a08;
  }
  * { box-sizing: border-box; margin: 0; padding: 0; }
  html, body { width: 1200px; height: 960px; overflow: hidden; }
  body {
    background: var(--page);
    font-family: "Open Sans", Arial, sans-serif;
    position: relative;
  }
  .card {
    position: absolute;
    top: 315px;
    width: 520px;
    height: 330px;
    border-radius: 20px;
    overflow: hidden;
  }
  /* Front */
  .card-front {
    left: 50px;
    background: linear-gradient(160deg, var(--card-dark-2), var(--card-dark));
  }
  .card-front .wave { position: absolute; inset: 0; width: 100%; height: 100%; }
  .region-label {
    position: absolute; left: 34px; top: 28px;
    color: var(--text-light); font-size: 15px; letter-spacing: 0.5px;
  }
  .world-map {
    position: absolute; left: 90px; top: 62px; width: 370px; height: 170px;
    border-radius: 40px;
    background: radial-gradient(ellipse at center, var(--map-grey) 0%, rgba(75,76,80,0.5) 55%, rgba(75,76,80,0) 75%);
  }
  .brand-name {
    position: absolute; right: 34px; top: 96px;
    color: var(--brand-blue-mid); font-weight: 700; font-size: 40px; letter-spacing: -1px;
    display: flex; align-items: center; gap: 8px;
  }
  .brand-dot { width: 14px; height: 14px; border-radius: 50%; background: var(--brand-blue-mid); }
  .card-number {
    position: absolute; left: 34px; top: 160px;
    font-family: "Share Tech Mono", monospace; font-size: 37px; letter-spacing: 2px;
    color: var(--emboss); text-shadow: 1px 1px 0 #777, -1px -1px 0 #fff3;
    word-spacing: 6px;
  }
  .valid {
    position: absolute; left: 60px; top: 214px; color: var(--text-light);
  }
  .valid-label { font-size: 7px; letter-spacing: 0.5px; display: block; }
  .valid-date { font-size: 14px; }
  .card-code {
    position: absolute; right: 40px; top: 215px; color: var(--text-muted); font-size: 12px;
  }
  .holder {
    position: absolute; right: 50px; bottom: 30px;
    color: var(--text-light); font-size: 26px; letter-spacing: 1px;
  }
  /* Back */
  .card-back {
    left: 630px;
    background: linear-gradient(180deg, var(--back-orange-1) 0%, var(--back-orange-1) 50%, var(--back-orange-2) 100%);
  }
  .magnetic-stripe {
    position: absolute; left: 0; right: 0; top: 28px; height: 58px; background: var(--stripe);
  }
  .terms {
    position: absolute; left: 30px; right: 30px; top: 104px;
    color: var(--back-text); font-size: 12.5px; line-height: 1.55;
  }
  .web {
    position: absolute; right: 34px; bottom: 30px;
    color: var(--back-text); font-weight: 700; font-size: 16px;
  }
</style>
</head>
<body>
  <section class="card card-front" aria-label="Tarjeta Europe, anverso">
    <div class="world-map" role="img" aria-label="Mapa del mundo en puntos grises"></div>
    <svg class="wave" viewBox="0 0 520 330" preserveAspectRatio="none" aria-hidden="true">
      <defs>
        <linearGradient id="navyBand" x1="0" y1="0" x2="1" y2="1">
          <stop offset="0" stop-color="#1b2e44"/>
          <stop offset="1" stop-color="#0255a3"/>
        </linearGradient>
      </defs>
      <path d="M0 200 C 110 250, 300 215, 520 260 L520 330 L0 330 Z" fill="var(--accent-orange)"/>
      <path d="M0 208 C 120 262, 310 236, 520 282 L520 330 L0 330 Z" fill="url(#navyBand)"/>
    </svg>
    <div class="region-label">EUROPE</div>
    <div class="brand-name"><span class="brand-dot"></span>verdapump</div>
    <div class="card-number">1234 4567 1234 4567</div>
    <div class="valid"><span class="valid-label">VALID THRU</span><span class="valid-date">01/18</span></div>
    <div class="card-code">0123</div>
    <div class="holder">MARTA LINDQVIST</div>
  </section>

  <section class="card card-back" aria-label="Tarjeta Europe, reverso">
    <div class="magnetic-stripe"></div>
    <p class="terms">
      La tarjeta VERDAPUMP ha sido emitida y es propiedad de VERDAPUMP
      S.L.U. y a requerimiento debe ser devuelta inmediatamente.
      El uso de esta tarjeta implica la aceptación de lo que indica el
      contrato entre las partes.
      En caso de pérdida, avise inmediatamente en el
      teléfono o en la siguiente dirección:
    </p>
    <div class="web">www.verdapump.es</div>
  </section>
</body>
</html>
```